The Harbourline Aid Trust needs a graphic of their innovation approach

What we need?
- we have designed a new innovation approach (see attached). An innovation approach is the process one goes through in order to design and launch a new product or service.
- This new graphic will be used in meetings to help others understand what innovation is and how we do it. It will also be used in training sessions and be the starting point for innovation training materials we are creating
- We have created this draft graphic by copying and pasting new words over another charities innovation process
- We would like you to use your design magic and create our very own innovation process graphic. We would like it to be neat, simple, non fussy, easy to understand /read and in line with our brand colours
Attached:
1. PowerPoint:
- Slide 1: our innovation process
- Slide 2 explanation of process to bring it to life
- Slide 3&4: brand colours
- Slide 5: inspiration / examples of other processes we like the look of
2. Typeface brand guidelines
We can't wait to see what you come up with! Thank you :)
internal employees
Charity

```html
<!DOCTYPE html>
<html lang="en">
<head>
<meta charset="utf-8">
<title>The Harbourline Aid Trust — Innovation Approach</title>
<link rel="stylesheet" href="https://fonts.googleapis.com/css2?family=Arimo:wght@700&display=swap">
<style>
  :root {
    --blue: #168fc2;
    --red: #e3191b;
    --orange: #f5a81c;
    --navy: #1b2f52;
    --track: #ebecee;
    --bg: #ffffff;
  }
  html, body {
    margin: 0;
    padding: 0;
    width: 1200px;
    height: 999px;
    overflow: hidden;
    background: var(--bg);
  }
  .process-map {
    display: block;
    width: 1200px;
    height: 999px;
    font-family: "Arimo", Arial, sans-serif;
    font-weight: 700;
  }
  .track { fill: none; stroke: var(--track); stroke-width: 22; }
  .path { fill: none; stroke-width: 15; stroke-linejoin: round; }
  .path--discover { stroke: var(--blue); }
  .path--define { stroke: var(--red); }
  .path--deliver { stroke: var(--orange); }
  .milestone { fill: var(--navy); }
  .milestone-label { fill: var(--navy); font-size: 22px; }
  .step { font-size: 17px; }
  .step--discover { fill: var(--blue); }
  .step--define { fill: var(--red); }
  .step--deliver { fill: var(--orange); }
  .stage-title { font-size: 25px; text-anchor: middle; }
  .stage-title--discover { fill: var(--blue); }
  .stage-title--define { fill: var(--red); }
  .stage-title--deliver { fill: var(--orange); }
  .icon { fill: none; stroke-width: 4.5; stroke-linecap: round; }
</style>
</head>
<body>
<svg class="process-map" viewBox="0 0 1200 999" xmlns="http://www.w3.org/2000/svg" role="img" aria-label="Innovation approach: Discover, Define, Deliver">
  <defs>
    <radialGradient id="hub-fill" cx="50%" cy="40%" r="60%">
      <stop offset="0%" stop-color="#fafafa"/>
      <stop offset="100%" stop-color="#e3e3e3"/>
    </radialGradient>
  </defs>

  <!-- background tracks -->
  <circle class="track" cx="380" cy="493" r="144"/>
  <circle class="track" cx="820" cy="493" r="144"/>
  <circle class="track" cx="600" cy="325" r="138"/>

  <!-- stage hubs -->
  <circle cx="380" cy="493" r="108" fill="url(#hub-fill)"/>
  <circle cx="600" cy="325" r="108" fill="url(#hub-fill)"/>
  <circle cx="820" cy="493" r="108" fill="url(#hub-fill)"/>

  <!-- journey path -->
  <path class="path path--discover" d="M33,493 H236 A144,144 0 0 0 524,493"/>
  <path class="path path--define" d="M524,486 L524,462 C524,425 466,405 463,350 A138,138 0 1 1 737,350 C734,405 676,425 676,470 L676,493 A144,144 0 0 0 686,545"/>
  <path class="path path--deliver" d="M686,545 A144,144 0 0 0 964,493 H1168"/>

  <!-- milestones -->
  <circle class="milestone" cx="154" cy="493" r="15"/>
  <circle class="milestone" cx="444" cy="616" r="15"/>
  <circle class="milestone" cx="600" cy="188" r="15"/>
  <circle class="milestone" cx="738" cy="320" r="15"/>
  <circle class="milestone" cx="1030" cy="493" r="15"/>

  <text class="milestone-label" x="95" y="466">Challenge</text>
  <text class="milestone-label" x="530" y="648" text-anchor="middle">Opportunity</text>
  <text class="milestone-label" x="530" y="676" text-anchor="middle">Statement</text>
  <text class="milestone-label" x="600" y="163" text-anchor="middle">Concepts</text>
  <text class="milestone-label" x="763" y="329">Pilot</text>
  <text class="milestone-label" x="986" y="465">Launch</text>

  <!-- steps along the path -->
  <text class="step step--discover" transform="translate(236,593) rotate(38)">Insight</text>
  <text class="step step--discover" transform="translate(540,572) rotate(-75)">Ideate</text>
  <text class="step step--define" transform="translate(446,296) rotate(-65)">(In) validate</text>
  <text class="step step--define" transform="translate(688,190) rotate(42)">Test</text>
  <text class="step step--define" transform="translate(652,472) rotate(82)">Iterate</text>
  <text class="step step--deliver" transform="translate(752,652) rotate(10)">Delivery Plan</text>

  <!-- Discover icon: magnifier -->
  <g class="icon" stroke="var(--blue)">
    <circle cx="393" cy="450" r="24"/>
    <line x1="375" y1="468" x2="344" y2="496" stroke-width="9"/>
  </g>
  <text class="stage-title stage-title--discover" x="380" y="535">Discover</text>

  <!-- Define icon: target with pencil -->
  <g class="icon" stroke="var(--red)">
    <circle cx="600" cy="292" r="34"/>
    <circle cx="600" cy="292" r="22"/>
    <circle cx="600" cy="292" r="10"/>
    <line x1="604" y1="288" x2="664" y2="264" stroke-width="8"/>
  </g>
  <text class="stage-title stage-title--define" x="600" y="368">Define</text>

  <!-- Deliver icon: bulb with arrow -->
  <g class="icon" stroke="var(--orange)">
    <circle cx="816" cy="448" r="20"/>
    <path d="M806,466 L806,494 H826 L826,466"/>
    <line x1="800" y1="412" x2="806" y2="422"/>
    <line x1="820" y1="406" x2="820" y2="418"/>
    <line x1="840" y1="412" x2="834" y2="422"/>
    <path d="M782,460 C810,470 840,462 866,440" stroke-width="6"/>
    <path d="M852,438 L870,436 L864,452" stroke-width="5"/>
  </g>
  <text class="stage-title stage-title--deliver" x="820" y="535">Deliver</text>
</svg>
</body>
</html>
```